To design a new professional and elegant website design

To design an elegant and professional business website - e.g. Responsive WordPress theme.

Please refer to the existing site www.merrow-partners.example for information regarding the business service and the content that will be included.

While the designer can suggest colors, the current logo (see attached) should remain.
Although I have indicated Sans Serif as a font, I welcome alternative suggestions.
Updates

To all designers:

I have attached additional .psd files of the logo for your use in the design of the new site (theme). As posted in an earlier response, I wish to keep the logo and the color blue. You are welcome to either work with or change the green.

- Please avoid making the page too busy.

- Avoid stock business pictures such as the people working on a document with the calculator the generic people in suits. Ideally, I would like unique media.

- Do not include contact information on the home page. There are two offices – 1 in Houston and one in UK and I want to make sure that we distinguish between the two.

- Use bullets rather than check boxes .

- Do not use the social links as we do not currently use them - this may change in the future

- The footer should include: sitemap, Terms of Use, Privacy Policy and the 2014 Copyright notice. The other pages should be accessible via a menu

Hope this helps.
Thanks

To all participants,

I have increased the budget by an additional £200.

Regards,

Target Market(s)

As you may glean from the website, the company is a management consultancy serving Pinnacle 400 companies and private equity firms. Companies include: Lorn, GQ, TW, Varnell Orbe Companies, Kel Mordan...

Sites that may influence the design include:

http://www.qvd.example.co.uk/consulting/
http://www.jn.example/UK/en/Services/Advisory
http://www.holt.example/industry-expertise/technology/index.aspx
http://www.plovabranding.example/news

Industry/Entity Type

Business Service

Font styles to use
Sans Serif

Colors

Designer to choose colors to be used in the design.

Requirements
Must have
• Existing blue logo - globe with the M & P (see attached). The green is not necessary
Must function of a WordPress responsive platform.
Nice to have
• While the new theme will need to be consistent throughout the site, the home page can vary from the child pages.
Should not have
• Common stock images. If used, the images and icons should be unique.

```html
<!DOCTYPE html>
<html lang="en">
<head>
<meta charset="utf-8">
<title>Merrow Partners</title>
<link rel="stylesheet" href="https://fonts.googleapis.com/css2?family=Arimo:ital,wght@0,400;0,700;1,400&display=swap">
<style>
:root{
  --blue-deep:#1e76e2;
  --blue-light:#5ea8f2;
  --blue-text:#2b8de8;
  --blue-footer:#2a7fe6;
  --green:#3cd63c;
  --green-soft:#8de37a;
  --mint:#d8ecd6;
  --panel:#ececec;
  --ink:#222;
  --ink-soft:#333;
  --rule:#c9c9c9;
  --white:#fff;
}
*{box-sizing:border-box;margin:0;padding:0}
html,body{width:1200px;height:800px;overflow:hidden;background:var(--white)}
body{position:relative;font-family:"Arimo",Arial,sans-serif;color:var(--ink)}
.abs{position:absolute}

.site-header{position:absolute;left:0;top:0;width:1200px;height:116px;
  background:linear-gradient(180deg,var(--blue-deep) 0%,var(--blue-light) 100%)}
.brand{left:10px;top:18px;display:flex;align-items:center;gap:14px}
.brand-mark{width:72px;height:72px;border-radius:50%;background:#e9eef3}
.brand-name{font-size:25px;font-weight:700;color:#3b3f44;letter-spacing:2px;line-height:25px}
.tagline{left:362px;top:40px;font-size:15px;font-style:italic;color:var(--green)}
.search{left:957px;top:28px;width:208px;height:25px;background:#f2f2f2;border:1px solid #c8c8c8;
  font-size:13px;color:#9a9a9a;padding:5px 8px}
.search svg{position:absolute;right:6px;top:4px}
.main-nav{left:531px;top:92px;display:flex;font-size:13px;color:var(--white)}
.main-nav a{color:inherit;text-decoration:none;text-align:center;height:24px;line-height:16px;border-right:1px solid rgba(255,255,255,.6)}
.main-nav a:last-child{border-right:0}
.main-nav .current{color:var(--green)}

.hero{left:17px;top:133px;width:775px;height:260px;
  background:linear-gradient(90deg,#7d8086 0%,#4a4c50 40%,#4a4c50 70%,#3c49b0 88%,#d8def2 100%)}
.hero-line{left:338px;top:192px;font-size:17px;color:var(--green-soft);line-height:28px}
.hero-line b{font-weight:400;font-size:22px}
.hero-dots{left:734px;top:373px;display:flex;gap:9px}
.hero-dots i{width:8px;height:8px;border-radius:50%;border:1px solid #fff}
.hero-dots i.on{background:#fff}
.solutions{left:792px;top:133px;width:372px;height:260px;background:var(--panel);border:1px solid #e0e0e0;padding:22px 26px}
.solutions h2{font-size:22px;font-weight:400;color:var(--blue-text);margin-bottom:32px}
.solutions p{font-size:12px;line-height:14.6px;color:var(--ink);margin-bottom:14px}
.solutions .rule{position:absolute;left:26px;right:0;top:235px;border-top:1px solid #d8d8d8}

.section-bar{top:409px;height:34px;background:var(--mint);font-size:17px;color:var(--blue-text);line-height:34px;font-weight:400}
.news{left:17px;top:460px;width:352px}
.news-item{position:relative;height:78px;margin-bottom:17px;border-bottom:1px solid var(--rule);padding:2px 10px 0 14px}
.news-item::before{content:"";position:absolute;left:1px;top:5px;width:6px;height:6px;background:var(--blue-text)}
.news-item h3{font-size:12.5px;font-weight:700;color:var(--ink-soft);margin-bottom:4px}
.news-item time{position:absolute;right:9px;top:2px;font-size:11px;color:var(--ink-soft)}
.news-item p{font-size:12px;line-height:15px;color:var(--ink-soft)}
.news-item .more{position:absolute;right:23px;top:55px;font-size:12px;color:var(--blue-text)}
.news-item .more::after{content:"";position:absolute;right:-9px;top:3px;border-left:5px solid var(--blue-text);border-top:4px solid transparent;border-bottom:4px solid transparent}

.expertise{left:439px;top:461px;list-style:none}
.expertise li{position:relative;padding-left:16px;font-size:12.5px;height:24.4px;color:var(--ink-soft)}
.expertise li::before{content:"";position:absolute;left:0;top:4px;width:6px;height:6px;background:var(--blue-text)}

.clients-intro{left:784px;top:459px;width:340px;font-size:12px;line-height:14.6px;color:var(--ink)}
.sectors{left:784px;top:518px;list-style:none}
.sectors li{display:flex;align-items:center;height:26.2px;font-size:12.5px;color:var(--ink-soft)}
.sectors svg{width:18px;height:18px;margin-right:13px}

.site-footer{position:absolute;left:0;top:758px;width:1200px;height:42px;background:var(--blue-footer);color:var(--white);font-size:13.5px}
.footer-nav{left:12px;top:5px;display:flex}
.footer-nav a{color:inherit;text-decoration:none;padding:0 10px;height:22px;line-height:16px;border-right:1px solid rgba(255,255,255,.6)}
.footer-nav a:last-child{border-right:0}
.copyright{right:12px;top:6px}
</style>
</head>
<body>
<header class="site-header">
  <div class="brand abs"><span class="brand-mark"></span><span class="brand-name">MERROW<br>PARTNERS</span></div>
  <p class="tagline abs">Where Strategy, Operations and People Deliver Performance</p>
  <div class="search abs">Search
    <svg width="16" height="16" viewBox="0 0 16 16"><circle cx="6.5" cy="6.5" r="4.5" fill="none" stroke="#8a8a8a" stroke-width="2"/><line x1="10" y1="10" x2="14.5" y2="14.5" stroke="#8a8a8a" stroke-width="2.5"/></svg>
  </div>
  <nav class="main-nav abs">
    <a class="current" style="width:76px">Home</a><a style="width:86px">About</a><a style="width:82px">Values</a><a style="width:164px">Clients and Services</a><a style="width:90px">Join Us</a><a style="width:75px">FAQ</a><a style="width:86px">Contact</a>
  </nav>
</header>

<div class="hero abs" role="img" aria-label="Illustration of figures in blue and green joining hands around a wire globe, beside a large globe with marked locations"></div>
<p class="hero-line abs">We <b>Partner</b> with <b>Our Clients</b><br>to <b>Deliver Results</b></p>
<div class="hero-dots abs"><i class="on"></i><i></i><i></i></div>

<section class="solutions abs">
  <h2>Consulting Solutions</h2>
  <p>We work alongside your teams and leverage our experience to deliver simple but pragmatic solutions to complex business issues at a lower cost than traditional consulting firms. We leave you with a heritage of capabilities and tools needed to sustain results.</p>
  <p>We combine advisory services with interim managers and executives to provide the most effective support to your businesses needs.</p>
  <div class="rule"></div>
</section>

<h2 class="section-bar abs" style="left:17px;width:356px;padding-left:15px">News and Events</h2>
<h2 class="section-bar abs" style="left:387px;width:336px;padding-left:28px">Merrow's Expertise</h2>
<h2 class="section-bar abs" style="left:738px;width:426px;padding-left:46px">Clients</h2>

<div class="news abs">
  <article class="news-item"><h3>Lorem ipsum dolor sit amet</h3><time>Feb 07, 2014</time><p>Ut enim ad minim veniam, quis nostrud exercitation ullamco laboris nisi ut aliquip ex ea commodo consequat...</p><a class="more">more</a></article>
  <article class="news-item"><h3>Lorem ipsum dolor sit amet</h3><time>Feb 06, 2014</time><p>Ut enim ad minim veniam, quis nostrud exercitation ullamco laboris nisi ut aliquip ex ea commodo consequat...</p><a class="more">more</a></article>
  <article class="news-item"><h3>Lorem ipsum dolor sit amet</h3><time>Feb 05, 2014</time><p>Ut enim ad minim veniam, quis nostrud exercitation ullamco laboris nisi ut aliquip ex ea commodo consequat...</p><a class="more">more</a></article>
</div>

<ul class="expertise abs">
  <li>Due Diligence</li><li>Portfolio Growth</li><li>Cost Reduction</li><li>Strategic Planning</li><li>Organizational Alignment</li><li>Governance</li><li>Project Office</li><li>Process Reengineering</li><li>Process Automation</li><li>Outsourcing</li>
</ul>

<p class="clients-intro abs">We have supported a range of clients, from the small start-up to the global Pinnacle 400, generate revenue, productivity and cost gains in specific services and sectors.</p>
<ul class="sectors abs">
  <li><svg viewBox="0 0 18 18"><path d="M2 15 L15 3 L16 5 L5 16Z" fill="#1e8fe0"/><path d="M6 6 L13 9 L10 12Z" fill="#3cc43c"/></svg>Transport</li>
  <li><svg viewBox="0 0 18 18"><circle cx="10" cy="9" r="6" fill="none" stroke="#3cc43c" stroke-width="2"/><circle cx="7" cy="10" r="3.5" fill="#1e8fe0"/></svg>Energy and Environment</li>
  <li><svg viewBox="0 0 18 18"><path d="M1 4 H4 L6 12 H15 L16 6 H5" fill="none" stroke="#1e8fe0" stroke-width="2"/><circle cx="7" cy="15" r="1.5" fill="#1e8fe0"/><circle cx="14" cy="15" r="1.5" fill="#1e8fe0"/></svg>FMCG</li>
  <li><svg viewBox="0 0 18 18"><rect x="2" y="2" width="7" height="15" fill="#1e8fe0"/><rect x="10" y="7" width="6" height="10" fill="#3cc43c"/></svg>Government</li>
  <li><svg viewBox="0 0 18 18"><path d="M1 17 V6 L6 9 V5 L11 9 V4 H15 V17Z" fill="#1e8fe0"/></svg>Mining</li>
  <li><svg viewBox="0 0 18 18"><circle cx="9" cy="9" r="3" fill="#1e8fe0"/><circle cx="3" cy="3" r="2" fill="#3cc43c"/><circle cx="15" cy="3" r="2" fill="#3cc43c"/><circle cx="3" cy="15" r="2" fill="#3cc43c"/><circle cx="15" cy="15" r="2" fill="#3cc43c"/></svg>Healthcare</li>
  <li><svg viewBox="0 0 18 18"><rect x="2" y="2" width="14" height="14" fill="#3cc43c"/><rect x="5" y="5" width="8" height="8" fill="#1e8fe0"/></svg>Technology</li>
  <li><svg viewBox="0 0 18 18"><path d="M3 3 Q1 9 9 16 L12 13 L9 10 L7 11 Q5 9 6 7 L7 6 L5 2Z" fill="#1e8fe0"/><path d="M10 3 A5 5 0 0 1 15 8" fill="none" stroke="#3cc43c" stroke-width="2"/></svg>Telecom and Media</li>
</ul>

<footer class="site-footer">
  <nav class="footer-nav abs"><a>Sitemap</a><a>Terms of Use</a><a>Privacy Policy</a></nav>
  <p class="copyright abs">All Rights Reserved. Merrow-Partners LCC 2014</p>
</footer>
</body>
</html>
```